Promotional brochure for educational consulting firm

Updates

Hi Designers!

Please do a 8.5 x 11 inch tri-fold brochure as well as a 8.5 x 11 inch half-fold brochure.  I appreciate black and white versions in addition to color.  Please take a look at my company's website for a better sense of the look and feel I am going for:  www.brightlarkco.org

Thanks!

Industry/Entity Type

Consulting

Colors
3176b5
85abd2
fcfbfd

```html
<!DOCTYPE html>
<html lang="en">
<head>
<meta charset="utf-8">
<title>Brightlark Associates – Tri-fold Brochure</title>
<link href="https://fonts.googleapis.com/css2?family=Open+Sans:wght@400;600;700&family=Tinos:wght@400;700&display=swap" rel="stylesheet">
<style>
  :root{
    --black:#000000;
    --blue:#0d5aa7;
    --bright-blue:#1e9be0;
    --text-blue:#1f5fae;
    --pale:#e6e6e6;
    --grey:#bbbcc0;
    --body-grey:#555555;
    --white:#ffffff;
    --page:#ffffff;
  }
  *{box-sizing:border-box;margin:0;padding:0}
  html,body{width:1200px;height:1002px;overflow:hidden;background:var(--page)}
  body{position:relative;font-family:"Open Sans",Arial,sans-serif}
  .spread{position:absolute;left:297px;width:597px;display:flex}
  .spread--outside{top:28px;height:458px}
  .spread--inside{top:503px;height:463px}
  .panel{position:relative;width:199px;height:100%;overflow:hidden}

  /* outside */
  .panel--contact{background:var(--black);color:var(--white);text-align:center}
  .contact{position:absolute;top:272px;left:0;width:100%;font-size:7.5px;font-weight:600;line-height:10.5px}
  .contact__title{margin-bottom:11px}
  .brand-mini{position:absolute;top:370px;left:0;width:100%;display:flex;align-items:center;justify-content:center;gap:5px;font-size:8px;font-weight:700;color:var(--blue)}
  .brand-mini__dot{width:9px;height:9px;border-radius:50%;background:var(--blue)}

  .panel--tagline{background:var(--pale);text-align:center}
  .tagline{position:absolute;top:210px;width:100%;font-family:"Tinos","Times New Roman",serif;font-size:18px;line-height:25px;color:#111}
  .tagline__em{display:block;color:var(--blue);font-weight:700;font-size:19px}

  .panel--cover{background:var(--blue)}
  .cover__grey{position:absolute;top:0;left:0;width:100%;height:174px;background:var(--grey)}
  .cover__white{position:absolute;top:174px;left:0;width:100%;height:114px;background:var(--white);display:flex;align-items:center;justify-content:center;gap:6px}
  .brand{font-size:10.5px;font-weight:700;color:var(--blue);letter-spacing:.3px}
  .brand__dot{width:12px;height:12px;border-radius:50%;background:var(--blue)}

  /* inside */
  .strip{position:absolute;left:0;width:100%;height:21px}
  .strip--top{top:0}
  .strip--bottom{bottom:0}
  .strip--grey{background:var(--grey)}
  .strip--blue{background:var(--blue)}
  .panel--intro,.panel--questions{background:var(--white)}
  .panel--intro{border-left:1px solid #e2e2e2}
  .deco-circle{position:absolute;top:56px;left:76px;width:42px;height:42px;border-radius:50%;border:5px solid #dadada}
  .intro{position:absolute;left:25px;width:150px;font-size:7.4px;line-height:11px;color:var(--body-grey);text-align:justify}
  .intro--lead{top:118px}
  .intro--lead strong{color:var(--text-blue);font-weight:400}
  .intro--body{top:163px;letter-spacing:.15px}
  .art{position:absolute}
  .art--growth{left:0;top:100px;width:145px;height:310px;top:auto;bottom:52px;height:150px;background:linear-gradient(160deg,#bfe3a0 0%,#f0e0a8 45%,#eeeeee 100%);border-radius:4px}
  .art--question{left:52px;top:52px;width:104px;height:117px;background:linear-gradient(180deg,#eef6fc 0%,#cfe6f7 60%,#f4f4f4 100%);border-radius:6px}

  .questions{position:absolute;left:22px;top:180px;width:162px;font-size:7.2px;line-height:9.6px;color:var(--text-blue)}
  .questions p{margin-bottom:8.6px}
  .questions p.tight{margin-bottom:0}

  .panel--bio{background:var(--black);color:var(--white)}
  .portrait{position:absolute;left:64px;top:45px;width:71px;height:91px;border:3px solid #9a9a9a;background:linear-gradient(180deg,#8a8a8a 0%,#5c5c5c 100%)}
  .bio__name{position:absolute;top:138px;width:100%;text-align:center;font-size:8.5px;font-weight:700;color:var(--bright-blue)}
  .bio__role{position:absolute;top:149px;width:100%;text-align:center;font-size:6.8px;font-style:italic}
  .bio__text{position:absolute;top:176px;left:28px;width:145px;font-size:7.2px;line-height:10px;text-align:justify}
  .bio__text strong{color:var(--bright-blue);font-weight:700}
  .expertise__title{position:absolute;top:282px;left:28px;font-size:9.5px;font-weight:700;color:var(--bright-blue)}
  .expertise{position:absolute;top:300px;left:28px;list-style:none;font-size:7px}
  .expertise li{display:flex;align-items:center;gap:6px;height:14.8px}
  .expertise svg{flex:none}
</style>
</head>
<body>

<section class="spread spread--outside">
  <div class="panel panel--contact">
    <div class="contact">
      <p class="contact__title">Contact Us</p>
      <p>Dana Whitcomb, Ed.D.</p>
      <p>[t]&nbsp; 555.014.2271</p>
      <p>[f]&nbsp; 555.014.3390</p>
      <p>dana@brightlarkco.org</p>
      <p>www.brightlarkco.org</p>
    </div>
    <div class="brand-mini"><span class="brand-mini__dot"></span>Brightlark Associates LLC</div>
  </div>
  <div class="panel panel--tagline">
    <p class="tagline">School leadership is <span class="tagline__em">24/7/365</span></p>
  </div>
  <div class="panel panel--cover">
    <div class="cover__grey"></div>
    <div class="cover__white"><span class="brand__dot"></span><span class="brand">Brightlark Associates LLC</span></div>
  </div>
</section>

<section class="spread spread--inside">
  <div class="panel panel--intro">
    <div class="strip strip--top strip--grey"></div>
    <div class="deco-circle"></div>
    <p class="intro intro--lead"><strong>Brightlark Associates</strong> provides just-in-time support to schools and school leaders.</p>
    <p class="intro intro--body">Schools along the continuum of organizational growth from startup schools to developing or mature schools can benefit from specialized expertise to complete a time-sensitive special project or develop strategies and processes to take their program to the next level of excellence.</p>
    <div class="art art--growth" role="img" aria-label="Illustration of figures beneath a rising green arrow"></div>
    <div class="strip strip--bottom strip--blue"></div>
  </div>

  <div class="panel panel--questions">
    <div class="strip strip--top strip--blue"></div>
    <div class="art art--question" role="img" aria-label="Illustration of a figure beside a question mark sign"></div>
    <div class="questions">
      <p>How do I develop a high-functioning board?</p>
      <p>What policies do start-up schools need to have on day one?</p>
      <p>Is my meal program optimizing revenue?</p>
      <p>We want to refinance our property. How do we tell our story to a lender?</p>
      <p>How can we increase parent engagement?</p>
      <p>What do we need to do to increase visibility (and enrollment)?</p>
      <p class="tight">My assistant principal is going out on extended leave… can I get someone to step in while he's out?</p>
      <p>Do these questions keep you up at night? If so, we can help.</p>
    </div>
    <div class="strip strip--bottom strip--grey"></div>
  </div>

  <div class="panel panel--bio">
    <div class="portrait" role="img" aria-label="Portrait photograph of the founder"></div>
    <p class="bio__name">Dana Whitcomb, Ed.D.</p>
    <p class="bio__role">Founder &amp; CEO</p>
    <p class="bio__text">My 10-year experience as an executive director of charter schools in the two largest school districts in California gives me a unique <strong>"education + business"</strong> perspective in addition to a network of on-call, expert associates who are ready to assist your school in a variety of key areas.</p>
    <p class="expertise__title">Our areas of expertise include:</p>
    <ul class="expertise">
      <li><svg width="8" height="8" viewBox="0 0 8 8"><circle cx="4" cy="4" r="3.3" fill="none" stroke="#1e9be0" stroke-width="1.2"/></svg>Board Training</li>
      <li><svg width="8" height="8" viewBox="0 0 8 8"><circle cx="4" cy="4" r="3.3" fill="none" stroke="#1e9be0" stroke-width="1.2"/></svg>Budget and Operations</li>
      <li><svg width="8" height="8" viewBox="0 0 8 8"><circle cx="4" cy="4" r="3.3" fill="none" stroke="#1e9be0" stroke-width="1.2"/></svg>Charter Development</li>
      <li><svg width="8" height="8" viewBox="0 0 8 8"><circle cx="4" cy="4" r="3.3" fill="none" stroke="#1e9be0" stroke-width="1.2"/></svg>Communications</li>
      <li><svg width="8" height="8" viewBox="0 0 8 8"><circle cx="4" cy="4" r="3.3" fill="none" stroke="#1e9be0" stroke-width="1.2"/></svg>Leadership Coaching</li>
      <li><svg width="8" height="8" viewBox="0 0 8 8"><circle cx="4" cy="4" r="3.3" fill="none" stroke="#1e9be0" stroke-width="1.2"/></svg>Lender Negotiations</li>
      <li><svg width="8" height="8" viewBox="0 0 8 8"><circle cx="4" cy="4" r="3.3" fill="none" stroke="#1e9be0" stroke-width="1.2"/></svg>Fund Development</li>
      <li><svg width="8" height="8" viewBox="0 0 8 8"><circle cx="4" cy="4" r="3.3" fill="none" stroke="#1e9be0" stroke-width="1.2"/></svg>Placement of interim administrators</li>
    </ul>
  </div>
</section>

</body>
</html>
```